Branding for Clearflow Honours program collateral

The Clearflow Honours, hosted by the Aqueduct Trade Union, are an annual awards program to recognise excellence in the Australian water industry. The awards presentation ceremony is held over a formal luncheon, with a MC and Keynote Speaker. The awards event is a premium experience for business professionals that work in the work sector. It is a corporate business luncheon with management level professionals in attendance. We are seeking branding design elements that we can use on all awards collateral including the website, printed invitation, event program, social media posts etc. The Clearflow Honours are well known in the industry and recognised by its logo and corporate colours (attached). We would like these incorporated into the design.

Target Market(s)

business professionals

Industry/Entity Type

Water Company

Requirements
Must have
• event logo, corporate colours

```html
<!DOCTYPE html>
<html lang="en">
<head>
<meta charset="utf-8">
<title>Clearflow Honours – Cover</title>
<link rel="stylesheet" href="https://fonts.googleapis.com/css2?family=Montserrat:wght@500&display=swap">
<style>
  :root {
    --page-bg: #ffffff;
    --leaf-green: #80bd59;
    --sea-teal: #5aa9a3;
    --water-blue: #2a9fd8;
    --deep-blue: #1f86b8;
    --bloom-pink: #d55aa8;
    --sun-orange: #f39322;
    --type-white: #ffffff;
  }
  html, body {
    margin: 0;
    width: 1200px;
    height: 1200px;
    overflow: hidden;
    background: var(--page-bg);
  }
  .canvas {
    position: relative;
    width: 1200px;
    height: 1200px;
  }
  .cover {
    position: absolute;
    left: 279px;
    top: 62px;
    width: 715px;
    height: 968px;
    overflow: hidden;
    background:
      linear-gradient(155deg, transparent 72%, rgba(243,147,34,0) 72%),
      linear-gradient(150deg, var(--leaf-green) 0%, var(--sea-teal) 40%, #4aa6bf 60%, var(--water-blue) 72%, #8f8ac0 80%, var(--bloom-pink) 86%, var(--deep-blue) 87%);
    box-shadow: 2px 2px 4px rgba(0,0,0,0.12);
  }
  .cover__corner {
    position: absolute;
    right: 0;
    bottom: 0;
    width: 0;
    height: 0;
    border-left: 260px solid transparent;
    border-bottom: 60px solid var(--sun-orange);
  }
  .cover__splash {
    position: absolute;
    left: 0;
    top: 270px;
    width: 715px;
    height: 698px;
  }
  .brand {
    position: absolute;
    left: 0;
    right: 0;
    top: 228px;
    text-align: center;
    color: var(--type-white);
    font-family: "Montserrat", sans-serif;
    font-weight: 500;
  }
  .brand__name {
    margin: 0;
    font-size: 40px;
    letter-spacing: 1px;
    line-height: 1;
    transform: translateX(16px);
  }
  .brand__region {
    margin: 34px 0 0;
    font-size: 14px;
    letter-spacing: 3.5px;
    transform: translateX(16px);
  }
</style>
</head>
<body>
<div class="canvas">
  <section class="cover">
    <svg class="cover__splash" viewBox="0 0 715 698" role="img" aria-label="Rising water splash illustration over a flowing wave">
      <defs>
        <radialGradient id="splashTone" cx="0.62" cy="0.55" r="0.6">
          <stop offset="0" stop-color="#7cc6ec" stop-opacity="0.75"/>
          <stop offset="0.6" stop-color="#3eaee2" stop-opacity="0.45"/>
          <stop offset="1" stop-color="#3eaee2" stop-opacity="0"/>
        </radialGradient>
        <linearGradient id="waveTone" x1="0" y1="0" x2="1" y2="0">
          <stop offset="0" stop-color="#6fc0ea" stop-opacity="0.7"/>
          <stop offset="0.6" stop-color="#3aa6da" stop-opacity="0.8"/>
          <stop offset="1" stop-color="#1f86b8"/>
        </linearGradient>
      </defs>
      <rect x="330" y="0" width="385" height="560" fill="url(#splashTone)"/>
      <path d="M0 560 C 150 520, 300 560, 460 560 S 650 500, 715 470 L 715 698 L 0 698 Z" fill="url(#waveTone)"/>
    </svg>
    <div class="cover__corner"></div>
    <header class="brand">
      <h1 class="brand__name">Clearflow Honours</h1>
      <p class="brand__region">SOUTH AUSTRALIA</p>
    </header>
  </section>
</div>
</body>
</html>
```